SnackHarbor!!! A Vending Machine Business Looking for an attractive website.

We are a vending machine business in Northern Michigan. We have changed our name and have rebranded our company. We would like an attractive website that shares who we are, what services we provide, the products we offer in our machines, along with a form businesses can fill out to see if they are a good fit for our company. I would like to have a Home Page, About SnackHarbor, Why Choose SnackHarbor?, Products & Services, Contact Us (With a Login Option), and a page with a questionnaire for thos interested in getting a FREE Vending Machine.

Target Market(s)

Businesses, Campgrounds, Schools, and many more in Northern Michigan

Industry/Entity Type

Vending Machines

Number of Pages Required

5+ page

Requirements
Must have
• An inviting and enticing Home Page. I want to get my potential clients engaged in our website.
Nice to have
• Possibly background photos from Northern Michigan
Should not have
• A corporate feel. I do not want a boring website.

```html
<!DOCTYPE html>
<html lang="en">
<head>
<meta charset="utf-8">
<title>SnackHarbor – Vending in Northern Michigan</title>
<link rel="stylesheet" href="https://fonts.googleapis.com/css2?family=Itim&family=Poppins:wght@400;500;600&display=swap">
<style>
  :root {
    --navy: #1f2163;
    --green: #4f9136;
    --green-dark: #3a6a2c;
    --grey-bg: #f0f0f0;
    --line: #d9d9d9;
    --text: #333;
    --muted: #666;
    --white: #fff;
    --head: "Itim", cursive;
    --body: "Poppins", sans-serif;
  }
  * { box-sizing: border-box; margin: 0; padding: 0; }
  html, body { width: 1200px; height: 3670px; overflow: hidden; background: var(--white); }
  body { font-family: var(--body); color: var(--text); }
  section, header, footer { position: relative; width: 1200px; overflow: hidden; }
  .abs { position: absolute; }
  .brand { font-family: var(--head); color: var(--navy); display: flex; align-items: center; gap: 8px; white-space: nowrap; }
  .brand-mark { width: 22px; height: 22px; background: var(--green); border-radius: 4px; flex: none; }
  .pill { display: inline-block; border-radius: 30px; font-weight: 600; font-size: 11px; color: var(--white); text-align: center; white-space: nowrap; }
  .pill-green { background: var(--green); }
  .pill-navy { background: var(--navy); }
  .eyebrow { font-family: var(--head); color: var(--green); font-size: 19px; text-align: center; width: 100%; }
  .title { font-family: var(--head); font-weight: 400; font-size: 40px; text-align: center; width: 100%; }

  /* header */
  .site-header { height: 95px; border-bottom: 1px solid #eee; }
  .site-header .brand { left: 106px; top: 24px; font-size: 34px; }
  .topbar-item { top: 7px; font-size: 10px; color: var(--muted); white-space: nowrap; }
  .free-tab { left: 895px; top: 0; width: 195px; height: 26px; background: var(--green-dark); color: var(--white); font-size: 11px; font-weight: 500; text-align: center; line-height: 26px; clip-path: polygon(4% 0, 100% 0, 96% 100%, 0 100%); }
  .nav { left: 477px; top: 54px; display: flex; gap: 36px; font-size: 11px; font-weight: 600; color: var(--navy); white-space: nowrap; }
  .nav .active { color: var(--green); border-bottom: 2px solid var(--green); padding-bottom: 16px; }
  .login { left: 999px; top: 45px; width: 95px; height: 32px; line-height: 32px; }

  /* hero */
  .hero { height: 1040px; background: var(--navy); }
  .hero-photo { left: 0; top: 0; width: 1200px; height: 640px; background: linear-gradient(180deg, #4a4a48 0%, #5c5a4d 30%, #3e4f4a 60%, #2d3b3e 100%); }
  .hero-h1 { left: 106px; top: 170px; font-family: var(--head); font-weight: 400; color: var(--white); font-size: 44px; }
  .hero-sub { left: 106px; top: 225px; font-family: var(--head); color: var(--white); font-size: 29px; }
  .hero-cta { left: 106px; top: 274px; width: 190px; height: 34px; line-height: 34px; }
  .machine-shot { left: 745px; top: 52px; width: 285px; height: 580px; background: linear-gradient(180deg, #3b3f6d 0%, #7c8fb8 55%, #a9adb2 80%, #7d7f83 100%); border-radius: 6px 6px 80px 80px; }
  .welcome-eyebrow { top: 690px; }
  .welcome-title { top: 720px; color: var(--white); }
  .welcome-text { left: 250px; top: 786px; width: 700px; color: #e6e6f2; font-size: 11px; line-height: 19px; text-align: center; }
  .welcome-cta { left: 532px; top: 880px; width: 136px; height: 34px; line-height: 34px; }

  /* products */
  .products { height: 665px; }
  .products .eyebrow { position: absolute; top: 80px; }
  .products .title { position: absolute; top: 108px; color: var(--navy); }
  .card { top: 322px; width: 250px; height: 225px; border: 1px solid var(--line); border-top: none; }
  .card::before, .card::after { content: ""; position: absolute; top: 0; height: 1px; width: 40px; background: var(--line); }
  .card::before { left: 0; } .card::after { right: 0; }
  .card-halo { top: 200px; width: 150px; height: 150px; border-radius: 50%; background: #f3f3f3; }
  .card-shot { top: 185px; width: 120px; height: 190px; border-radius: 4px; }
  .card h3 { position: absolute; top: 128px; width: 100%; text-align: center; font-family: var(--head); font-weight: 400; color: var(--navy); font-size: 19px; }
  .card p { position: absolute; top: 158px; left: 20px; width: 210px; text-align: center; font-size: 9px; line-height: 13px; color: var(--muted); }
  .card .pill { position: absolute; left: 56px; bottom: -18px; width: 138px; height: 34px; line-height: 34px; }
  .arrow-btn { width: 30px; height: 30px; border: 1px solid #999; border-radius: 50%; background: var(--white); display: flex; align-items: center; justify-content: center; }

  /* why choose */
  .why { height: 620px; }
  .why-photo { left: 0; top: 0; width: 1200px; height: 620px; background: linear-gradient(180deg, #3d6c2f 0%, #457a35 50%, #3a6a2c 100%); }
  .why-eyebrow { top: 70px; color: var(--white); font-family: var(--head); font-size: 18px; text-align: center; width: 100%; }
  .why-title { top: 96px; color: var(--white); }
  .feature h4 { font-family: var(--head); font-weight: 400; color: var(--white); font-size: 18px; line-height: 20px; margin-bottom: 12px; }
  .feature p { color: #e8f0e4; font-size: 10px; line-height: 18px; }
  .feature.left { text-align: right; }
  .feature-icon { width: 52px; height: 52px; border-radius: 50%; background: var(--white); display: flex; align-items: center; justify-content: center; }
  .feature-icon span { width: 34px; height: 34px; border-radius: 50%; background: var(--navy); display: flex; align-items: center; justify-content: center; }
  .center-badge { left: 500px; top: 228px; width: 200px; height: 200px; border-radius: 50%; background: var(--white); border: 12px solid var(--green); display: flex; align-items: center; justify-content: center; }
  .center-badge .brand { font-size: 24px; gap: 6px; }
  .center-badge .brand-mark { width: 16px; height: 16px; }
  .why-cta { left: 536px; top: 512px; width: 128px; height: 34px; line-height: 34px; }

  /* clients */
  .clients { height: 310px; }
  .clients .title { position: absolute; top: 50px; color: var(--navy); }
  .client-row { left: 212px; top: 120px; display: flex; gap: 12px; }
  .client { width: 119px; height: 66px; border: 1px solid #e3e3e3; display: flex; align-items: center; justify-content: center; font-family: var(--head); color: var(--navy); font-size: 17px; white-space: nowrap; }

  /* signup */
  .signup { height: 565px; }
  .signup-photo { left: 0; top: 0; width: 1200px; height: 565px; background: linear-gradient(180deg, #2a2d6c 0%, #23265f 60%, #1d1f55 100%); }
  .signup-eyebrow { top: 255px; }
  .signup-title { top: 282px; left: 350px; width: 500px; color: var(--white); font-size: 30px; line-height: 37px; }
  .signup-text { left: 300px; top: 372px; width: 600px; text-align: center; color: #e6e6f2; font-size: 12px; line-height: 18px; }
  .email-field { left: 330px; top: 430px; width: 425px; height: 36px; border-radius: 20px; background: var(--white); font-size: 9px; color: #777; padding-left: 18px; line-height: 36px; }
  .submit { left: 768px; top: 430px; width: 100px; height: 36px; line-height: 36px; }

  /* footer */
  .site-footer { height: 350px; background: var(--grey-bg); }
  .site-footer > .brand { left: 200px; top: 95px; font-size: 34px; }
  .col-title { font-family: var(--head); color: var(--navy); font-size: 14px; margin-bottom: 18px; }
  .contact-line { display: flex; gap: 10px; align-items: flex-start; font-size: 10px; color: var(--navy); margin-bottom: 16px; white-space: nowrap; }
  .contact-line.big { font-size: 14px; }
  .links p { font-size: 9px; color: var(--navy); margin-bottom: 12px; white-space: nowrap; }
  .social { left: 972px; top: 60px; display: flex; flex-direction: column; gap: 10px; }
  .social span { width: 28px; height: 28px; border-radius: 50%; background: var(--navy); }
  .social span:nth-child(2) { background: var(--green); }
  .copyright { left: 200px; top: 255px; font-size: 9px; color: var(--navy); }
  .copyright b { color: var(--green); font-weight: 500; }
  .back-to-top { left: 1100px; top: 245px; }
</style>
</head>
<body>

<header class="site-header">
  <div class="abs brand"><span class="brand-mark"></span>SnackHarbor</div>
  <span class="abs topbar-item" style="left:617px">&#9742; 555-014-2290</span>
  <span class="abs topbar-item" style="left:730px">&#9993; info@snackharbor-mi.com</span>
  <div class="abs free-tab">Get a Free Vending Machine</div>
  <nav class="abs nav">
    <span class="active">Home</span><span>About Us</span><span>Why Choose Us?</span><span>Products &amp; Services</span><span>Contact Us</span>
  </nav>
  <div class="abs pill pill-navy login">&#9787; Log In</div>
</header>

<section class="hero">
  <div class="abs hero-photo" role="img" aria-label="Aerial evening photo of a Northern Michigan harbour town with marina boats"></div>
  <h1 class="abs hero-h1">Crave. Vend. Repeat.</h1>
  <p class="abs hero-sub">Elevating Snacking, One Vend at a Time</p>
  <div class="abs pill pill-green hero-cta">Get a Free Vending Machine</div>
  <div class="abs machine-shot" role="img" aria-label="Snack vending machine standing on a silver round pedestal"></div>
  <svg class="abs" style="left:0;top:440px" width="1200" height="320" viewBox="0 0 1200 320">
    <path d="M0 170 C180 50 360 60 520 150 C700 250 900 280 1200 150 L1200 320 L0 320 Z" fill="var(--green)"/>
    <path d="M0 200 C180 80 360 90 520 175 C700 270 900 300 1200 175 L1200 320 L0 320 Z" fill="var(--navy)"/>
  </svg>
  <p class="abs eyebrow welcome-eyebrow">Who We Are</p>
  <h2 class="abs title welcome-title">Welcome to SnackHarbor</h2>
  <p class="abs welcome-text">Where snacking meets delight! We're not just about vending machines; we're your culinary companions, your flavor curators, and your secret stash of happiness. Marla and Owen, the dynamic duo behind SnackHarbor, have a passion for all things tasty. With backgrounds in sales and a penchant for personal connections, they've transformed the vending experience into an art form.</p>
  <div class="abs pill pill-green welcome-cta">Explore More</div>
</section>

<section class="products">
  <p class="eyebrow">What We Offer</p>
  <h2 class="title">Products &amp; Services</h2>

  <div class="abs card-halo" style="left:249px"></div>
  <div class="abs card-halo" style="left:524px"></div>
  <div class="abs card-halo" style="left:801px"></div>

  <div class="abs card" style="left:200px">
    <h3>Drink Machine</h3>
    <p>It is a long established fact that a reader will be distracted by the readable.</p>
    <div class="pill pill-navy">Get a Free Quote</div>
  </div>
  <div class="abs card" style="left:475px">
    <h3>Candy &amp; Snack Machine</h3>
    <p>It is a long established fact that a reader will be distracted by the readable.</p>
    <div class="pill pill-green">Get a Free Quote</div>
  </div>
  <div class="abs card" style="left:752px">
    <h3>Cold Food Machine</h3>
    <p>It is a long established fact that a reader will be distracted by the readable.</p>
    <div class="pill pill-navy">Get a Free Quote</div>
  </div>

  <div class="abs card-shot" style="left:264px;background:linear-gradient(180deg,#cfd6e4,#5b7fc4 70%,#9aa0a8)" role="img" aria-label="Glass-front drink vending machine"></div>
  <div class="abs card-shot" style="left:540px;background:linear-gradient(180deg,#3b3f6d,#7894c8 70%,#a6aab0)" role="img" aria-label="Candy and snack vending machine"></div>
  <div class="abs card-shot" style="left:816px;background:linear-gradient(180deg,#4a4a4a,#6d6d6d 60%,#bfbfbf)" role="img" aria-label="Cold food vending machine"></div>

  <div class="abs arrow-btn" style="left:184px;top:420px"><svg width="10" height="10" viewBox="0 0 10 10"><path d="M6.5 1.5 3 5l3.5 3.5" fill="none" stroke="#333" stroke-width="1.4"/></svg></div>
  <div class="abs arrow-btn" style="left:987px;top:420px"><svg width="10" height="10" viewBox="0 0 10 10"><path d="M3.5 1.5 7 5 3.5 8.5" fill="none" stroke="#333" stroke-width="1.4"/></svg></div>
</section>

<section class="why">
  <div class="abs why-photo" role="img" aria-label="Aerial photo of Northern Michigan forest and lakeshore with green tint"></div>
  <p class="abs why-eyebrow">SnackHarbor</p>
  <h2 class="abs title why-title">Why Choose Us</h2>

  <div class="abs feature left" style="left:150px;top:170px;width:258px">
    <h4>Local Love</h4>
    <p>We celebrate the heart of Michigan by partnering with local legends. Say hello to Birchwood Jerky and Pine Shore Potato Chips—our hometown heroes.</p>
  </div>
  <div class="abs feature" style="left:793px;top:170px;width:262px">
    <h4>Unleash Your Cravings</h4>
    <p>SnackHarbor isn't bound by corporate ties. We're the rebels of the vending world. Craving a bag of crispy, kettle-cooked chips? Done. Hankering for jerky that packs a punch?...</p>
  </div>
  <div class="abs feature left" style="left:150px;top:370px;width:258px">
    <h4>Quality Meets Convenience</h4>
    <p>Imagine this: You're mid-meeting, and your stomach growls. Fear not! SnackHarbor's machines offer top-notch snacks and beverages...</p>
  </div>
  <div class="abs feature" style="left:793px;top:370px;width:280px">
    <h4>Pandemic-Proof &amp;<br>Recession-Ready</h4>
    <p>Life throws curveballs, but SnackHarbor stands strong. Our vending machines are the unsung heroes of resilience...</p>
  </div>

  <svg class="abs" style="left:470px;top:198px" width="260" height="260" viewBox="0 0 260 260">
    <path d="M45 80 A100 100 0 0 0 45 180" fill="none" stroke="var(--white)" stroke-width="2"/>
    <path d="M215 80 A100 100 0 0 1 215 180" fill="none" stroke="var(--white)" stroke-width="2"/>
    <path d="M80 45 A100 100 0 0 1 100 36" fill="none" stroke="var(--white)" stroke-width="2"/>
    <path d="M180 45 A100 100 0 0 0 160 36" fill="none" stroke="var(--white)" stroke-width="2"/>
    <path d="M80 215 A100 100 0 0 0 100 224" fill="none" stroke="var(--white)" stroke-width="2"/>
    <path d="M180 215 A100 100 0 0 1 160 224" fill="none" stroke="var(--white)" stroke-width="2"/>
  </svg>
  <div class="abs center-badge"><div class="brand"><span class="brand-mark"></span>SnackHarbor</div></div>

  <div class="abs feature-icon" style="left:435px;top:196px"><span><svg width="14" height="14" viewBox="0 0 14 14"><path d="M7 1a4 4 0 0 1 4 4c0 3-4 8-4 8S3 8 3 5a4 4 0 0 1 4-4z" fill="#fff"/></svg></span></div>
  <div class="abs feature-icon" style="left:713px;top:196px"><span><svg width="14" height="14" viewBox="0 0 14 14"><rect x="2" y="5" width="10" height="7" rx="1" fill="#fff"/><rect x="4" y="2" width="6" height="3" fill="#fff"/></svg></span></div>
  <div class="abs feature-icon" style="left:435px;top:408px"><span><svg width="14" height="14" viewBox="0 0 14 14"><circle cx="7" cy="6" r="4" fill="none" stroke="#fff" stroke-width="1.6"/><path d="M5 10l-1 3 3-1 3 1-1-3" fill="#fff"/></svg></span></div>
  <div class="abs feature-icon" style="left:713px;top:408px"><span><svg width="14" height="14" viewBox="0 0 14 14"><rect x="3" y="1" width="8" height="12" rx="1" fill="none" stroke="#fff" stroke-width="1.4"/><path d="M5 5h4M5 8h4" stroke="#fff" stroke-width="1.2"/></svg></span></div>

  <div class="abs pill pill-navy why-cta">Explore More</div>
</section>

<section class="clients">
  <h2 class="title">Our Clients</h2>
  <div class="abs client-row">
    <div class="client">Crispo Puffs</div>
    <div class="client">Nutta Bar</div>
    <div class="client">Dotties</div>
    <div class="client">Crust Captain</div>
    <div class="client">Zing Fuel</div>
    <div class="client">Bakewell</div>
  </div>
  <div class="abs arrow-btn" style="left:568px;top:222px"><svg width="10" height="10" viewBox="0 0 10 10"><path d="M6.5 1.5 3 5l3.5 3.5" fill="none" stroke="#333" stroke-width="1.4"/></svg></div>
  <div class="abs arrow-btn" style="left:604px;top:222px"><svg width="10" height="10" viewBox="0 0 10 10"><path d="M3.5 1.5 7 5 3.5 8.5" fill="none" stroke="#333" stroke-width="1.4"/></svg></div>
</section>

<section class="signup">
  <div class="abs signup-photo" role="img" aria-label="Evening street photo of a Northern Michigan downtown with blue tint"></div>
  <svg class="abs" style="left:0;top:0" width="1200" height="240" viewBox="0 0 1200 240">
    <path d="M0 0 H1200 V45 C1000 -10 820 60 640 150 C430 250 170 210 0 90 Z" fill="var(--green)"/>
    <path d="M0 0 H1200 V30 C1000 -20 820 40 640 130 C430 225 170 190 0 70 Z" fill="var(--white)"/>
  </svg>
  <p class="abs eyebrow signup-eyebrow">Sign Up Now!</p>
  <h2 class="abs title signup-title">Ready to experience the SnackHarbor difference?</h2>
  <p class="abs signup-text">Sign up now and let's connect. Taste the future of snacking firsthand! Contact us today and explore how our vending magic can elevate your space.</p>
  <div class="abs email-field">Enter your email...</div>
  <div class="abs pill pill-green submit">Submit</div>
</section>

<footer class="site-footer">
  <div class="abs brand"><span class="brand-mark"></span>SnackHarbor</div>
  <div class="abs" style="left:487px;top:60px">
    <p class="col-title">Contact Us</p>
    <p class="contact-line big"><span style="color:var(--green)">&#9742;</span>555-014-2290</p>
    <p class="contact-line"><span style="color:var(--green)">&#9993;</span>info@snackharbor-mi.com</p>
    <p class="contact-line"><svg width="10" height="12" viewBox="0 0 10 12"><path d="M5 0a4 4 0 0 1 4 4c0 3-4 8-4 8S1 7 1 4a4 4 0 0 1 4-4z" fill="var(--green)"/></svg><span>48 Cedar Bay Rd.,<br>Northport - 4967</span></p>
  </div>
  <div class="abs links" style="left:770px;top:60px">
    <p class="col-title">Quick Links</p>
    <p>Home</p><p>About Us</p><p>Why Choose Us?</p><p>Products &amp; Services</p><p>Contact Us</p>
  </div>
  <div class="abs social"><span></span><span></span><span></span></div>
  <p class="abs copyright">© 2024 <b>SnackHarbor</b>. All Right Reserved</p>
  <svg class="abs back-to-top" width="16" height="16" viewBox="0 0 16 16" aria-label="Back to top"><path d="M8 1 14 15 8 11 2 15Z" fill="var(--green)"/></svg>
</footer>

</body>
</html>
```